Rural photography business needs a 'car door magnet' design

I am a photographer with my main focus being on sheep shearers, shearing sheds and the country lifestyle.
I need a design for a car door magnet to advertise my business. My car is black so it needs to stand out from this.
Updates

can you please submit designs without my photo.

just include my logo, phone number and website, thanks.

Reason: I am now looking for designs that don't contain my photo. I would like a design that stands out against my black car door. It would be nice to have sheep in the picture or a camera.

Target Market(s)

My target audience is sheep shearers and other shearing shed workers and farmers. Age group would be between 25-50.

Industry/Entity Type

Business

Font styles to use
Script

Requirements
Must have
• Must have my uploaded logo, mobile number - 0471620394 and website address - www.brindalemoorphotography.example.

Nice to have
• If you are to include any sheep in the design can you please make sure they are merino
Should not have
• Pictures of people

```html
<!DOCTYPE html>
<html lang="en">
<head>
<meta charset="utf-8">
<title>Brindale Moor Photography – Car Door Magnet</title>
<link rel="stylesheet" href="https://fonts.googleapis.com/css2?family=Arimo:wght@700&display=swap">
<style>
  :root {
    --page-bg: #141414;
    --sky-top: #2f56c9;
    --sky-violet: #7a4fb0;
    --sunset-red: #d8442a;
    --sunset-orange: #f5861c;
    --sunset-gold: #fbb23a;
    --horizon: #b8321e;
    --grass-dark: #2f7f1f;
    --grass-mid: #58b52e;
    --grass-light: #86d640;
    --lens-outer: #4a4d52;
    --lens-inner: #8f9399;
    --fleece: #b9ab93;
    --text-light: #ffffff;
    --text-dark: #1e1e1e;
  }
  html, body {
    margin: 0;
    padding: 0;
    width: 1200px;
    height: 1000px;
    overflow: hidden;
    background: var(--page-bg);
  }
  .canvas {
    position: relative;
    width: 1200px;
    height: 1000px;
  }
  .magnet {
    position: absolute;
    left: 60px;
    top: 125px;
    width: 1080px;
    height: 750px;
    border-radius: 34px;
    overflow: hidden;
    background: linear-gradient(180deg,
      var(--sky-top) 0%,
      var(--sky-violet) 18%,
      var(--sunset-red) 32%,
      var(--sunset-orange) 42%,
      var(--sunset-gold) 52%,
      var(--horizon) 60%,
      var(--grass-dark) 64%,
      var(--grass-mid) 78%,
      var(--grass-light) 100%);
    font-family: "Arimo", Arial, sans-serif;
  }
  .lens-artwork {
    position: absolute;
    left: -35px;
    top: -40px;
    width: 660px;
    height: 660px;
    border-radius: 50%;
    background: radial-gradient(circle at 50% 50%,
      var(--fleece) 0%,
      var(--fleece) 52%,
      var(--lens-inner) 62%,
      var(--lens-outer) 72%,
      #2b2d30 100%);
  }
  .phone {
    position: absolute;
    right: 60px;
    top: 30px;
    display: flex;
    align-items: center;
    gap: 10px;
    color: var(--text-light);
    font-size: 56px;
    font-weight: 700;
    letter-spacing: 1px;
  }
  .phone svg { width: 48px; height: 54px; }
  .brand-mark {
    position: absolute;
    left: 790px;
    top: 175px;
    width: 190px;
    height: 190px;
    box-sizing: border-box;
    border: 10px solid var(--text-light);
    border-radius: 50%;
  }
  .business-name {
    position: absolute;
    left: 400px;
    top: 420px;
    width: 660px;
    text-align: center;
    color: var(--text-dark);
    font-size: 62px;
    font-weight: 700;
    line-height: 1.2;
  }
  .website {
    position: absolute;
    left: 0;
    right: 0;
    bottom: 30px;
    text-align: center;
    color: var(--text-light);
    font-size: 46px;
    font-weight: 700;
  }
</style>
</head>
<body>
<div class="canvas">
  <div class="magnet">
    <div class="lens-artwork" role="img" aria-label="Merino ram standing inside a large camera zoom lens"></div>

    <div class="phone">
      <svg viewBox="0 0 24 26" aria-hidden="true">
        <path fill="#ffffff" d="M6 2c1 0 2 .6 2.3 1.6l1 3.2c.3 1-.1 2-1 2.5l-1.5.9c.9 2.8 2.6 5.2 5 6.9l1.3-1.1c.8-.7 2-.7 2.8 0l2.6 2.2c.8.7.9 1.9.2 2.7l-1.5 1.8c-.9 1-2.4 1.4-3.7.9C7.3 21 2.7 14.5 2.2 6.8 2.1 4.3 3.7 2 6 2z"/>
      </svg>
      <span>0471620394</span>
    </div>

    <div class="brand-mark" aria-hidden="true"></div>

    <div class="business-name">BRINDALE MOOR<br>Photography</div>

    <div class="website">www.brindalemoorphotography.example</div>
  </div>
</div>
</body>
</html>
```